Company Profile
Korvane Cargo Sdn Bhd is a well-established and experienced freight forwarder in Kuala Lumpur, Malaysia. We specialize in air and sea forwarding, Custom Brokerage and regulatory compliance services, inland transportation, overseas freighting and warehousing and distribution management. With our dedicated qualified and experienced professionals, we are fully committed to serving our clients.

Our Mission
Based on the motto “Quick, Reliable and Polite”, Korvane Cargo is dedicated to upholding the following three points corporate philosophy:1. Adhering to the principle that “the customer always comes first”.2. Contributing to the development of the local community.3. Making it our duty to be responsible and sincere.

Our Edge
• One-Stop Logistics Solutions
• Extensive Network Throughout Malaysia
• Highly Qualified and Experienced Pool of Professionals
• Comprehensive IT Solutions
• Innovative and Customer-focused Solutions
• Flexible and Consistent in Managing Exceptions
• Total Supply Chain Visibility

Target Market : We sell the logistics services to all the industry in Malaysia. (One Stop Logistics Solutions)

Business Card Detail : I would like to see the logo on the front with the general info.

Must Haves :
1) Name, Title, Office, Cell, Fax, Email, Address, Website
2) Must have complete company name show as : Korvane Cargo Sdn Bhd
3) Must have company registration no, show as : 8571620-W

Nice to Haves : Modern Design Business Card

Target Market(s)

We sell the logistics services to all the industry in Malaysia. (One Stop Logistics Solutions)

Contact Information for Business Card

I would like to see the logo on the front with the general info.

Colors

Designer to choose colors to be used in the design.

Requirements
Must have
• 1) Name, Title, Office, Cell, Fax, Email, Address, Website
• 2) Must have complete company name show as : Korvane Cargo Sdn Bhd
• 3) Must have company registration no, show as : 8571620-W
Nice to have
• Modern Design Business Card
Should not have
• Nil

```html
<!DOCTYPE html>
<html lang="en">
<head>
<meta charset="utf-8">
<title>Korvane Cargo Business Card</title>
<link rel="stylesheet" href="https://fonts.googleapis.com/css2?family=Alegreya+Sans:wght@700&family=Arimo:wght@400;700&family=Roboto+Condensed:wght@500&display=swap">
<style>
  :root {
    --navy: #104383;
    --sky: #29a3dc;
    --paper: #ffffff;
    --ink: #111111;
    --stage: #000000;
  }
  * { margin: 0; padding: 0; box-sizing: border-box; }
  html, body { width: 1200px; height: 1200px; overflow: hidden; background: var(--stage); }
  .canvas { position: relative; width: 1200px; height: 1200px; }

  .card { position: absolute; width: 756px; height: 472px; background: var(--paper); overflow: hidden; }
  .card--front { left: 228px; top: 74px; }
  .card--back { left: 226px; top: 611px; }

  .band { position: absolute; left: 0; right: 0; bottom: 0; background: var(--navy); color: var(--paper); text-align: center; }
  .card--front .band { height: 112px; }
  .card--back .band { height: 113px; }

  .tagline {
    font-family: "Alegreya Sans", sans-serif; font-weight: 700; font-size: 23px;
    line-height: 112px; letter-spacing: 0.2px;
  }

  .brand { position: absolute; display: flex; align-items: center; gap: 26px; }
  .card--front .brand { left: 182px; top: 140px; }
  .card--back .brand { left: 182px; top: 41px; }
  .brand__dot { width: 84px; height: 84px; border-radius: 50%; border: 4px solid var(--navy); flex: none; }
  .brand__name {
    font-family: "Arimo", sans-serif; font-weight: 700; color: var(--navy);
    font-size: 38px; line-height: 40px; letter-spacing: 3px;
  }

  .person { position: absolute; left: 150px; top: 226px; }
  .person__name {
    font-family: "Roboto Condensed", sans-serif; font-weight: 500; color: var(--navy);
    font-size: 38px; line-height: 38px;
  }
  .person__title { font-family: "Arimo", sans-serif; font-size: 14px; color: var(--ink); margin-top: 2px; }

  .divider { position: absolute; left: 380px; top: 192px; width: 2px; height: 141px; background: var(--sky); }

  .contacts { position: absolute; left: 400px; top: 190px; list-style: none; }
  .contacts li {
    position: absolute; left: 0; display: flex; align-items: center; white-space: nowrap;
    font-family: "Arimo", sans-serif; font-size: 16.5px; color: var(--ink);
  }
  .contacts svg { width: 22px; height: 22px; margin-right: 10px; fill: none; stroke: var(--navy); stroke-width: 1.8; }
  .contacts .solid { fill: var(--navy); stroke: none; }

  .legal { font-family: "Arimo", sans-serif; font-size: 14.5px; }
  .legal__company { padding-top: 27px; }
  .legal__address { margin-top: 14px; line-height: 20px; }
</style>
</head>
<body>
<main class="canvas">

  <section class="card card--front" aria-label="Card front">
    <div class="brand">
      <span class="brand__dot"></span>
      <span class="brand__name">KORVANE<br>CARGO</span>
    </div>
    <div class="band"><p class="tagline">One Stop Logistics Specialist</p></div>
  </section>

  <section class="card card--back" aria-label="Card back">
    <div class="brand">
      <span class="brand__dot"></span>
      <span class="brand__name">KORVANE<br>CARGO</span>
    </div>

    <div class="person">
      <p class="person__name">AIDEN KOH</p>
      <p class="person__title">Managing Director</p>
    </div>

    <div class="divider"></div>

    <ul class="contacts">
      <li style="top:0">
        <svg viewBox="0 0 24 24"><rect x="7" y="2" width="10" height="20" rx="2"/><line x1="10" y1="18.5" x2="14" y2="18.5"/></svg>
        (+6012) 555 0147
      </li>
      <li style="top:33px">
        <svg viewBox="0 0 24 24"><path class="solid" d="M6.6 10.8a15 15 0 0 0 6.6 6.6l2.2-2.2c.3-.3.7-.4 1-.2 1.1.4 2.3.6 3.6.6.6 0 1 .4 1 1V20c0 .6-.4 1-1 1A17 17 0 0 1 3 4c0-.6.4-1 1-1h3.5c.6 0 1 .4 1 1 0 1.3.2 2.5.6 3.6.1.3 0 .7-.2 1z"/></svg>
        (+603) 5550 2143/2144
      </li>
      <li style="top:65px">
        <svg viewBox="0 0 24 24"><rect class="solid" x="7" y="2" width="10" height="5"/><rect class="solid" x="3" y="8" width="18" height="9" rx="1.5"/><rect x="7" y="13" width="10" height="8" fill="#fff"/><line x1="9" y1="16" x2="15" y2="16"/><line x1="9" y1="18.5" x2="15" y2="18.5"/></svg>
        (+603) 5550 2145
      </li>
      <li style="top:93px">
        <svg viewBox="0 0 24 24"><rect x="3" y="6" width="18" height="12"/><polyline points="3,6 12,13 21,6"/></svg>
        aiden.koh@korvanecargo.com.my
      </li>
      <li style="top:121px">
        <svg viewBox="0 0 24 24"><circle cx="12" cy="12" r="9"/><ellipse cx="12" cy="12" rx="4" ry="9"/><line x1="3" y1="12" x2="21" y2="12"/></svg>
        www.korvanecargo.com.my
      </li>
    </ul>

    <div class="band legal">
      <p class="legal__company">Korvane Cargo Sdn Bhd（8571620-W）</p>
      <p class="legal__address">No.27B, 2nd Floor, Jalan Seri Pantai 3/KS2, Taman Seri Pantai,<br>41050 Klang, Selangor Darul Ehsan, Malaysia.</p>
    </div>
  </section>

</main>
</body>
</html>
```